Brightvale Capital brochure for Investment partnership, young harold pemby

We need a brochure design to attract new investors for our investing partnership Called Brighttvale Capital. We are based in New Orleans, La. We primarily invest in stocks, bonds, and crypto but venture out into other categories as well. We would like to see designs with the black and gold like our logo. The final design should say new, fresh, sleek, tech, and honorable. BROUCHURE WILL BE 4 pages.or one folded sheet a paparer if that makes sense.

A chart showing Brighttvae Capital gains since 2019 28.6 percent and the KT 300 gAINS 7.1 PERCENT

Probable Investors

Financial Planning

• Black and Gold accent. Stock market feel. Sleek, High tech, innovative, Intellgent design.
• Page colors possibly black.
• Boring, Old school,

```html
<!DOCTYPE html>
<html lang="en">
<head>
<meta charset="utf-8">
<title>Brightvale Capital – Brochure</title>
<link href="https://fonts.googleapis.com/css2?family=EB+Garamond:wght@400;500;600&display=swap" rel="stylesheet">
<style>
  :root{
    --backdrop:#e3e3e3;
    --page:#000000;
    --ink:#ffffff;
    --ink-soft:#cfcfcf;
    --ink-muted:#8a8a8a;
    --gold:#e6b422;
    --gold-light:#f7dc6f;
    --gold-deep:#b8860b;
    --note:#ffffff;
    --note-ink:#333333;
    --yellow:#f2c230;
    --blue:#3d9be0;
    --green:#3dbb8c;
  }
  *{box-sizing:border-box;margin:0;padding:0}
  html,body{width:1200px;height:849px;overflow:hidden}
  body{background:var(--backdrop);font-family:"EB Garamond",Georgia,serif;position:relative;color:var(--ink)}

  .page{position:absolute;top:110px;width:440px;height:622px;background:var(--page);overflow:hidden;box-shadow:0 6px 18px rgba(0,0,0,.18)}
  .page--cover{left:135px}
  .page--inside{left:625px}

  /* Cover */
  .brand{position:absolute;top:70px;left:0;right:0;text-align:center;color:var(--ink);font-size:26px;font-weight:400;line-height:1}
  .cover__headline{position:absolute;top:124px;left:40px;right:40px;text-align:center;font-size:19px;font-weight:400;line-height:1.25;color:var(--ink)}
  .gold-rule{position:absolute;left:0;right:0;height:4px;background:linear-gradient(90deg,var(--gold-deep),var(--gold-light),var(--gold))}
  .gold-rule--top{top:218px}
  .cover__visual{position:absolute;top:222px;left:0;right:0;height:142px;background:radial-gradient(ellipse at 62% 45%,#5a5a5a 0%,#262626 45%,#0c0c0c 100%)}
  .cover__tagline{position:absolute;top:262px;left:34px;font-size:19px;line-height:1.2;color:var(--ink)}
  .gold-band{position:absolute;top:364px;left:0;right:0;height:22px;background:linear-gradient(90deg,var(--gold-deep),var(--gold-light) 40%,var(--gold) 70%,var(--gold-deep))}
  .cover__url{position:absolute;top:450px;left:0;right:0;text-align:center;font-size:18px;letter-spacing:1px;color:var(--ink-muted)}

  /* Inside */
  .intro{position:absolute;top:34px;left:38px;right:38px;font-size:9.5px;line-height:1.35;color:var(--ink-soft)}
  .section-title{position:absolute;top:98px;left:30px;right:30px;display:flex;align-items:center;gap:10px;font-size:13px;font-weight:400;color:var(--ink)}
  .section-title::before,.section-title::after{content:"";flex:1;border-top:1px dotted var(--ink-muted)}
  .steps{position:absolute;top:128px;left:22px;right:22px;display:flex;justify-content:space-between}
  .step{position:relative;width:118px;height:122px}
  .step:nth-child(2){margin-top:18px}
  .step:nth-child(3){margin-top:36px}
  .step__back{position:absolute;inset:6px -5px -6px 5px}
  .step--yellow .step__back{background:var(--yellow)}
  .step--blue .step__back{background:var(--blue)}
  .step--green .step__back{background:var(--green)}
  .step__card{position:absolute;inset:0;background:var(--note);padding:14px 18px 8px 10px;font-size:7.6px;line-height:1.3;color:var(--note-ink)}
  .step__num{position:absolute;top:12px;right:8px;font-size:13px;font-weight:600}
  .step--yellow .step__num{color:var(--yellow)}
  .step--blue .step__num{color:var(--blue)}
  .step--green .step__num{color:var(--green)}
  .step__clip{position:absolute;top:-8px;left:12px}
  .inside__photo{position:absolute;top:300px;left:0;right:0;height:122px;background:linear-gradient(100deg,#3a3a3a 0%,#9a9a9a 35%,#5c5c5c 60%,#c9c9c9 85%,#777 100%)}
  .about__title{position:absolute;top:438px;left:0;right:0;text-align:center;font-size:15px;font-weight:600;color:var(--ink)}
  .about__text{position:absolute;top:464px;left:40px;right:40px;text-align:center;font-size:9.5px;line-height:1.4;color:var(--ink-soft)}
</style>
</head>
<body>

<section class="page page--cover">
  <div class="brand">Brightvale Capital</div>
  <h1 class="cover__headline">Become a partner and build generational wealth by investing in the stock market</h1>
  <div class="gold-rule gold-rule--top"></div>
  <div class="cover__visual" role="img" aria-label="Hand holding a tablet displaying a rising stock chart, in black and white"></div>
  <p class="cover__tagline">A first of its kind<br>Investment Club</p>
  <div class="gold-band"></div>
  <p class="cover__url">www.brightvalecapital.com</p>
</section>

<section class="page page--inside">
  <p class="intro">If you are receiving this brochure its because someone sees you as a person that doesn't want to just work and pay bills. Your someone who wants to build real generational wealth. Not these schemes but the using the greatest wealth builder available: the stock market.</p>
  <h2 class="section-title">How it works</h2>

  <div class="steps">
    <article class="step step--yellow">
      <div class="step__back"></div>
      <div class="step__card">
        <span class="step__num">1</span>
        Make initial deposit. The general partner will invest in stocks, bonds and other investment vehicles on your behalf.
      </div>
      <svg class="step__clip" width="8" height="18" viewBox="0 0 8 18"><path d="M2 16V4a2 2 0 0 1 4 0v10" fill="none" stroke="#e0603c" stroke-width="1.3"/></svg>
    </article>
    <article class="step step--blue">
      <div class="step__back"></div>
      <div class="step__card">
        <span class="step__num">2</span>
        There is no upfront fees. The general partner will guarantee a 6 percent return and will work for free on your behalf until that is achieved. After the 6 percent return the limited partner will receive 80 percent and the general partner 20 percent of every dollar gained.
      </div>
      <svg class="step__clip" width="8" height="18" viewBox="0 0 8 18"><path d="M2 16V4a2 2 0 0 1 4 0v10" fill="none" stroke="#3d9be0" stroke-width="1.3"/></svg>
    </article>
    <article class="step step--green">
      <div class="step__back"></div>
      <div class="step__card">
        <span class="step__num">3</span>
        As the return and interests begins to compound annually, the legal partner legally owns shares of stock within the club and may redeem once a year or let money continue to earn interest.
      </div>
      <svg class="step__clip" width="8" height="18" viewBox="0 0 8 18"><path d="M2 16V4a2 2 0 0 1 4 0v10" fill="none" stroke="#3dbb8c" stroke-width="1.3"/></svg>
    </article>
  </div>

  <div class="inside__photo" role="img" aria-label="Black and white New Orleans street scene with historic balconies and a streetcar"></div>

  <h2 class="about__title">About Brightvale Capital and General Partner</h2>
  <p class="about__text">Brightvale Capital was founded in 2019 by General Partner Marcus Delaney Jr with a group economic empowerment mission. Marcus Delaney has invested in stocks since a teenager, received his BA in economics from Bayou Ridge University and is currently attending Pinecrest University.</p>
</section>

</body>
</html>
```